Business Card Design Project

We need a Business Card for an Mechanical Engineering firm in Singapore. The design should be Modern & Technical looking, yet eye catching.

Our company deals in Cutting Tools & Machine Accessories for the Manufacturing Industries such as Oil & Gas, Aero Space, etc... For more information on our Company, you can either email me or view our website www.torvale.com.sg.

We are trying to revamp our image to give our consumers a fresh new perspective to our company, so we welcome all ideas.

Industry/Entity Type

Business

Requirements
Must have
• Must incorporate New Company Logo into the card as shown in Uploaded file.

```html
<!DOCTYPE html>
<html lang="en">
<head>
<meta charset="utf-8">
<title>Torvale Tools – Business Card</title>
<link href="https://fonts.googleapis.com/css2?family=Exo+2:wght@400;500;600&display=swap" rel="stylesheet">
<style>
  :root {
    --bg-light: #f2eaed;
    --bg-mid: #dcc8cf;
    --bg-deep: #c8a8b3;
    --ink: #a0063c;
    --ink-dark: #4d0f24;
    --shadow: rgba(90, 20, 45, 0.35);
  }
  html, body {
    margin: 0;
    padding: 0;
    width: 1200px;
    height: 719px;
    overflow: hidden;
    background: #ffffff;
  }
  .card {
    position: relative;
    width: 1200px;
    height: 719px;
    overflow: hidden;
    background: linear-gradient(100deg, var(--bg-light) 0%, var(--bg-mid) 45%, var(--bg-deep) 100%);
    font-family: "Exo 2", sans-serif;
    color: var(--ink);
  }
  .identity {
    position: absolute;
    left: 82px;
    top: 70px;
    margin: 0;
  }
  .identity__name {
    margin: 0;
    font-size: 104px;
    font-weight: 600;
    line-height: 1;
    letter-spacing: 2px;
    text-shadow: 2px 3px 4px var(--shadow);
  }
  .identity__title {
    margin: 24px 0 0;
    font-size: 66px;
    font-weight: 600;
    line-height: 1;
    letter-spacing: 1px;
    text-shadow: 2px 3px 4px var(--shadow);
  }
  .contact {
    position: absolute;
    left: 84px;
    top: 318px;
    margin: 0;
    font-size: 31px;
    font-weight: 500;
    line-height: 45px;
    font-style: normal;
    text-shadow: 1px 2px 3px var(--shadow);
  }
  .contact__group + .contact__group {
    margin-top: 45px;
  }
  .contact p {
    margin: 0;
  }
  .brand {
    position: absolute;
    right: 16px;
    bottom: 22px;
    display: flex;
    align-items: center;
    gap: 18px;
  }
  .brand__mark {
    width: 82px;
    height: 82px;
    border-radius: 50%;
    background: var(--ink);
  }
  .brand__name {
    font-size: 80px;
    font-weight: 400;
    line-height: 1;
    letter-spacing: 1px;
    color: var(--ink-dark);
  }
</style>
</head>
<body>
  <main class="card">
    <header class="identity">
      <h1 class="identity__name">Your Name</h1>
      <h2 class="identity__title">Your Title</h2>
    </header>

    <address class="contact">
      <div class="contact__group">
        <p>Phone: 0092-00000</p>
        <p>Fax: 0092-00000</p>
      </div>
      <div class="contact__group">
        <p>Address</p>
        <p>City, State, ZIP</p>
        <p>email ID</p>
        <p>www.torvale.com.sg.</p>
      </div>
    </address>

    <div class="brand">
      <span class="brand__mark" aria-hidden="true"></span>
      <span class="brand__name">TORVALE TOOLS</span>
    </div>
  </main>
</body>
</html>
```